Design mobile friendly real estate and property management company landing page

Design a clean, crisp modern looking landing page that is mobile-friendly (must resize, preferably using bootstrap framework). Landing page will consist of heading with login area, company info, body consists of company description and services, a list of available rental properties with photos, and a footer with additional links and info. Working on updating with text for text areas marked A, B, and C on the layout pdf, but in meantime, lorem ipsum is fine. I can connect events to most buttons, etc. Just need the bootstrap and html functionality set up. Previous company website (which should not be relied upon) is www.qlbt.net This is somewhat of a template for a start, but looking for a more professional and modern design for the new website. But this gives an idea of the content and what needs to be displayed, and how.

Target Market(s)

Clients looking for a property management company that is efficient and well-organized.

Industry/Entity Type

Property Management

Coding

Coded - Design and coding required

Number of Pages Required

1 page

Font styles to use
Sans Serif

Colors
0355a3

Requirements
Must have
• Resize for the screen using bootstrap.
• Navigation that collapses for mobile devices
• Large text boxes and good solid spacing around all elements.
Nice to have
• for property images it would be nice if they can be swiped on touch enabled devices (to the next or previous image). And have navigation that can be clicked to next or previous images.
• Would be nice if a captcha verification was included on contact form.
Should not have
• Fancy or eccentric art

```html
<!DOCTYPE html>
<html lang="en">
<head>
<meta charset="utf-8">
<title>Northfield Realty Services</title>
<link href="https://fonts.googleapis.com/css2?family=Open+Sans:wght@400;600&display=swap" rel="stylesheet">
<style>
:root{
  --brand:#0355a3;
  --navy:#1a2340;
  --ink:#222;
  --muted:#9a9a9a;
  --line:#cfcfcf;
  --white:#fff;
  --black:#000;
}
*{box-sizing:border-box;margin:0;padding:0}
html,body{width:880px;height:1200px;overflow:hidden;background:var(--white)}
body{position:relative;font-family:'Open Sans',sans-serif;color:var(--ink)}
.abs{position:absolute}
.logo{left:138px;top:20px;width:156px;height:46px;background:var(--navy);outline:1px solid #fff;outline-offset:-4px;color:var(--white);display:flex;flex-direction:column;align-items:center;justify-content:center;font-size:11px;letter-spacing:1px;line-height:14px}
.find-label{left:350px;top:38px;font-size:8.5px;white-space:nowrap}
.find-input{left:410px;top:32px;width:121px;height:22px;border:1px solid #888;font-size:9px;padding:4px 6px}
.btn-search{left:539px;top:32px;width:86px;height:22px;background:var(--brand);color:var(--white);font-size:10px;text-align:center;line-height:22px}
.btn-login{left:682px;top:32px;width:60px;height:22px;border:2px solid var(--brand);font-size:9px;text-align:center;line-height:18px}
.nav{left:0;top:84px;width:880px;height:27px;background:var(--brand)}
.nav a{position:absolute;top:8px;color:var(--white);font-size:8.5px;text-decoration:none}
h2{position:absolute;font-weight:400;color:var(--brand);font-size:18px;white-space:nowrap}
.rule-left{height:2px;background:linear-gradient(90deg,var(--brand),rgba(3,85,163,0))}
.house{position:absolute;width:11px;height:11px}
.intro{left:138px;top:179px;width:392px;font-size:7.2px;line-height:14.4px}
.intro p+p{margin-top:14px}
.badge{top:322px;width:98px;height:76px;border:1.5px solid var(--brand);display:flex;align-items:center;justify-content:center}
.badge span{display:block;width:70px;height:40px;background:#d9dde6}
.form{left:554px;top:183px;width:188px;height:204px;border:5px solid #c8c8c8;background:var(--white)}
.field{position:absolute;left:9px;width:161px;height:19px;border:1px solid var(--line);background:#f7f7f7;font-size:6.5px;color:var(--muted);padding:4px 10px}
.btn-submit{left:608px;top:372px;width:81px;height:26px;background:var(--brand);color:var(--white);font-size:9px;text-align:center;line-height:26px}
.center-rule{left:285px;width:310px;height:12px}
.band{left:0;top:481px;width:880px;height:282px;background:linear-gradient(180deg,#6d8fb8 0%,#86a06c 45%,#3f7a2c 75%,#58a032 100%)}
.panel{top:481px;width:259px;height:282px;background:rgba(3,85,163,.88);color:var(--white);text-align:center}
.panel h3{font-weight:400;font-size:16px;margin-top:30px}
.panel .mini{display:block;margin:6px auto 0;width:170px;height:8px}
.panel p{font-size:6.8px;line-height:13.3px;margin:20px 10px 0}
.panel p+p{margin-top:13px}
.btn-more{position:absolute;left:69px;top:227px;width:121px;height:24px;background:var(--white);color:var(--brand);font-size:10px;line-height:24px}
.photo{left:138px;width:234px;height:139px;overflow:hidden}
.photo .tag{height:18px;background:var(--brand);color:var(--white);font-size:8px;text-align:center;line-height:18px}
.photo .img{height:121px}
.arrow{position:absolute;width:18px;height:22px;background:rgba(0,0,0,.55)}
.table{left:385px;width:357px;height:139px;border:1.5px solid var(--black);font-size:8px}
.table .head{position:absolute;left:0;top:0;width:100%;height:22px;line-height:21px;border-bottom:1.5px solid var(--black)}
.head span{position:absolute;top:0}
.head .divider{left:178px;height:100%;border-left:1.5px solid var(--black);padding-left:10px;white-space:nowrap}
.table .row{position:absolute;left:0;width:178px;height:29px;color:var(--white);font-size:7.5px}
.row span{position:absolute;top:9px}
.desc{position:absolute;left:183px;top:28px;width:168px;font-size:6.2px;line-height:16.5px}
.footer{left:0;top:1176px;width:880px;height:24px;background:var(--brand);color:var(--white);font-size:6.8px;text-align:center;line-height:24px}
</style>
</head>
<body>
<svg width="0" height="0" style="position:absolute">
  <symbol id="house" viewBox="0 0 12 12"><path d="M6 0.5 11.5 5.5H10V11.5H2V5.5H.5Z" fill="#0355a3"/><rect x="4.8" y="6.2" width="2.4" height="2.4" fill="#fff"/></symbol>
</svg>

<header>
  <div class="abs logo"><span>NORTHFIELD REALTY</span><span>SERVICES</span></div>
  <div class="abs find-label">Find a Home</div>
  <div class="abs find-input">City, Zip</div>
  <div class="abs btn-search">Search</div>
  <div class="abs btn-login">Login</div>
  <nav class="abs nav">
    <a style="left:230px">HOME</a><a style="left:283px">FOR RENT</a><a style="left:350px">FOR SALE</a>
    <a style="left:417px">PROPERTY MANAGEMENT</a><a style="left:543px">REAL ESTATE</a><a style="left:621px">ABOUT</a>
  </nav>
</header>

<section class="welcome">
  <h2 style="left:138px;top:130px">Welcome to Northfield Realty Services</h2>
  <svg class="house" style="left:138px;top:162px"><use href="#house"/></svg>
  <div class="abs rule-left" style="left:153px;top:167px;width:146px"></div>
  <div class="abs intro">
    <p>Lorem Ipsum is simply dummy text of the printing and typesetting industry. Lorem Ipsum has been the industry's standard dummy text ever since the 1500s, when an unknown printer took a galley of type and scrambled it to make a type specimen book. It has survived not only five centuries, but also the leap into electronic typesetting, remaining essentially unchanged.</p>
    <p>It was popularised in the 1960s with the release of Brightmark sheets containing Lorem Ipsum passages, and more recently with desktop publishing software like PressLayout Studio including versions of Lorem Ipsum. Lorem Ipsum is simply dummy text of the printing and typesetting industry.</p>
  </div>
  <div class="abs badge" style="left:178px"><span></span></div>
  <div class="abs badge" style="left:297px"><span></span></div>
  <div class="abs badge" style="left:416px"><span></span></div>
</section>

<section class="contact">
  <h2 style="left:554px;top:132px">Contact Us Form</h2>
  <svg class="house" style="left:554px;top:157px"><use href="#house"/></svg>
  <div class="abs rule-left" style="left:570px;top:163px;width:146px"></div>
  <div class="abs form">
    <div class="field" style="top:11px">Name</div>
    <div class="field" style="top:37px">Phone</div>
    <div class="field" style="top:62px">Email</div>
    <div class="field" style="top:87px">Subject Property</div>
    <div class="field" style="top:112px;height:53px">Comments</div>
  </div>
  <div class="abs btn-submit">SUBMIT</div>
</section>

<section class="services">
  <h2 style="left:408px;top:426px">Services</h2>
  <svg class="abs center-rule" style="top:453px" viewBox="0 0 310 12"><path d="M0 6H144M166 6H310" stroke="#0355a3" stroke-width="1.5"/><use href="#house" x="149" y="0" width="12" height="12"/></svg>
  <div class="abs band" role="img" aria-label="Suburban homes with green lawns and trees"></div>
  <div class="abs panel" style="left:159px">
    <h3>Property Management Services</h3>
    <svg class="mini" viewBox="0 0 170 8"><path d="M0 4H80M90 4H170" stroke="#fff" stroke-width=".8"/><path d="M85 .5 88.5 4H87.5V7.5H82.5V4H81.5Z" fill="#fff"/></svg>
    <p>Lorem Ipsum is simply dummy text of the printing and typesetting industry. Lorem Ipsum has been the industry's standard dummy text ever since the 1500s, when an unknown printer took a galley of type and scrambled it to make a type specimen book.</p>
    <p>It has survived not only five centuries, but also the leap into electronic typesetting, remaining essentially unchanged. It was popularised in the 1960s with the release of Brightmark sheets containing .</p>
    <div class="btn-more">REAM MORE</div>
  </div>
  <div class="abs panel" style="left:462px">
    <h3>Real / Estate Services</h3>
    <svg class="mini" viewBox="0 0 170 8"><path d="M0 4H80M90 4H170" stroke="#fff" stroke-width=".8"/><path d="M85 .5 88.5 4H87.5V7.5H82.5V4H81.5Z" fill="#fff"/></svg>
    <p>Lorem Ipsum is simply dummy text of the printing and typesetting industry. Lorem Ipsum has been the industry's standard dummy text ever since the 1500s, when an unknown printer took a galley of type and scrambled it to make a type specimen book.</p>
    <p>It has survived not only five centuries, but also the leap into electronic typesetting, remaining essentially unchanged. It was popularised in the 1960s with the release of Brightmark sheets containing .</p>
    <div class="btn-more">REAM MORE</div>
  </div>
</section>

<section class="listings">
  <h2 style="left:372px;top:792px">Featured Listings</h2>
  <svg class="abs center-rule" style="top:821px" viewBox="0 0 310 12"><path d="M0 6H144M166 6H310" stroke="#0355a3" stroke-width="1.5"/><use href="#house" x="149" y="0" width="12" height="12"/></svg>

  <div class="abs photo" style="top:862px">
    <div class="tag">For Rent</div>
    <div class="img" role="img" aria-label="Two-storey family house at dusk with lit windows" style="background:linear-gradient(180deg,#3d6aa8 0%,#8a7a6a 45%,#5a3a2a 70%,#2f4a22 100%)"></div>
    <svg class="arrow" style="left:0;top:66px" viewBox="0 0 18 22"><path d="M11 5 6 11 11 17" stroke="#fff" stroke-width="1.6" fill="none"/></svg>
    <svg class="arrow" style="right:0;top:66px" viewBox="0 0 18 22"><path d="M7 5 12 11 7 17" stroke="#fff" stroke-width="1.6" fill="none"/></svg>
  </div>
  <div class="abs table" style="top:862px">
    <div class="head"><span style="left:10px">Address</span><span class="divider">2 Bedroom, 1 Bath Condo</span></div>
    <div class="row" style="top:22px;background:var(--brand)"><span style="left:10px">Rent</span><span style="left:107px">Community</span></div>
    <div class="row" style="top:51px;background:var(--black)"><span style="left:10px">Date &nbsp;Avail</span><span style="left:107px">Parking</span></div>
    <div class="row" style="top:80px;background:var(--brand)"><span style="left:10px">Sqft</span><span style="left:107px">Pets</span></div>
    <div class="row" style="top:109px;height:28px;background:var(--black)"><span style="left:10px">Lease</span><span style="left:107px">Laundry</span></div>
    <div class="desc"><b style="font-weight:600">Discription:</b> Lorem Ipsum is simply dummy text of the printing and typesetting industry. Lorem Ipsum has been the industry's standard dummy text ever since the 1500s, when an unknown printer took a galley of type and scrambled it to make a type specimen book.</div>
  </div>

  <div class="abs photo" style="top:1014px">
    <div class="tag">For Rent</div>
    <div class="img" role="img" aria-label="Modern house at night with a lit swimming pool" style="background:linear-gradient(180deg,#1c2430 0%,#5a4a32 40%,#3a3528 65%,#1f4a55 100%)"></div>
    <svg class="arrow" style="left:0;top:66px" viewBox="0 0 18 22"><path d="M11 5 6 11 11 17" stroke="#fff" stroke-width="1.6" fill="none"/></svg>
    <svg class="arrow" style="right:0;top:66px" viewBox="0 0 18 22"><path d="M7 5 12 11 7 17" stroke="#fff" stroke-width="1.6" fill="none"/></svg>
  </div>
  <div class="abs table" style="top:1014px">
    <div class="head"><span style="left:10px">Address</span><span class="divider">2 Bedroom, 1 Bath Condo</span></div>
    <div class="row" style="top:22px;background:var(--brand)"><span style="left:10px">Rent</span><span style="left:107px">Community</span></div>
    <div class="row" style="top:51px;background:var(--black)"><span style="left:10px">Date &nbsp;Avail</span><span style="left:107px">Parking</span></div>
    <div class="row" style="top:80px;background:var(--brand)"><span style="left:10px">Sqft</span><span style="left:107px">Pets</span></div>
    <div class="row" style="top:109px;height:28px;background:var(--black)"><span style="left:10px">Lease</span><span style="left:107px">Laundry</span></div>
    <div class="desc" style="left:187px"><b style="font-weight:600">Discription:</b> Lorem Ipsum is simply dummy text of the printing and typesetting industry. Lorem Ipsum has been the industry's standard dummy text ever since the 1500s, when an unknown printer took a galley of type and scrambled it to make a type specimen book.</div>
  </div>
</section>

<footer class="abs footer">©2016 Northfield Realty Services | All Rights Reserved | Terms of Use and Privacy Policy</footer>
</body>
</html>
```